Professional IT Company Letterhead

We need a new letterhead design to incorporate our new login and business card design recently received here on Pixel Meadow. We want the same look and feel as the other two accepted projects. We want a professional and clean design.

Target Market(s)

Medical/Dental and Professional Services Businesses (CPA, Attorney, Architect etc)

Industry/Entity Type

Business

Requirements
Must have
• Clean and professional, consistent brand with our current design of our new logo and business cards.
Nice to have
• Would like to also be able to use the design on our newsletter header

```html
<!DOCTYPE html>
<html lang="en">
<head>
<meta charset="utf-8">
<title>Tidewater Systems Letterhead</title>
<link rel="stylesheet" href="https://fonts.googleapis.com/css2?family=Questrial&display=swap">
<style>
  :root {
    --backdrop: #ececec;
    --paper: #fcfcfc;
    --brand-sky: #27a9e1;
    --brand-ocean: #1475bd;
    --ink: #3a3a3a;
    --watermark: #f1f6fa;
  }
  html, body {
    margin: 0;
    width: 1200px;
    height: 1200px;
    overflow: hidden;
    background: var(--backdrop);
    font-family: "Questrial", "Century Gothic", sans-serif;
  }
  .letterhead {
    position: absolute;
    left: 210px;
    top: 48px;
    width: 754px;
    height: 1066px;
    background: var(--paper);
    transform: scale(1.0345);
    transform-origin: top left;
    box-shadow: 0 2px 8px rgba(0,0,0,0.12);
    overflow: hidden;
  }
  .brand {
    position: absolute;
    left: 64px;
    top: 62px;
  }
  .brand-row {
    display: flex;
    align-items: center;
    gap: 12px;
  }
  .brand-mark {
    width: 42px;
    height: 42px;
    border-radius: 50%;
    background: var(--brand-sky);
  }
  .brand-name {
    font-size: 30px;
    color: var(--brand-sky);
    letter-spacing: 0.2px;
    line-height: 1;
  }
  .brand-tagline {
    margin-top: 10px;
    font-size: 11px;
    letter-spacing: 0.9px;
    color: var(--brand-sky);
  }
  .water-line {
    position: absolute;
    left: 330px;
    top: 119px;
    width: 424px;
    height: 14px;
    background: linear-gradient(180deg, rgba(41,150,220,0) 0%, #3d9fdc 45%, #1c7fc9 60%, rgba(41,150,220,0) 100%);
  }
  .watermark {
    position: absolute;
    left: 10px;
    top: 340px;
    width: 570px;
    height: 400px;
    border-radius: 50%;
    background: radial-gradient(ellipse at center, var(--watermark) 0%, rgba(241,246,250,0) 70%);
  }
  .contact {
    position: absolute;
    left: 503px;
    top: 916px;
    font-size: 13.5px;
    color: var(--ink);
  }
  .contact-line {
    display: flex;
    align-items: center;
    gap: 9px;
    height: 18.5px;
  }
  .contact-line svg { width: 13px; height: 13px; fill: var(--brand-ocean); }
  .address {
    margin-top: 16px;
    line-height: 19px;
  }
  .footer-waves {
    position: absolute;
    left: 0;
    bottom: 0;
    width: 754px;
    height: 116px;
  }
</style>
</head>
<body>
  <main class="letterhead">
    <header class="brand">
      <div class="brand-row">
        <span class="brand-mark"></span>
        <span class="brand-name">Tidewater Systems</span>
      </div>
      <div class="brand-tagline">IT Support for Medical &amp; Dental Practices</div>
    </header>

    <div class="water-line" role="img" aria-label="Splashing water surface line"></div>

    <div class="watermark" role="img" aria-label="Faint brand emblem watermark area"></div>

    <section class="contact">
      <div class="contact-line">
        <svg viewBox="0 0 16 16"><path d="M2 5c0-2 2-3 6-3s6 1 6 3v1h-3V5H5v1H2zM4 7h8l2 6H2z"/></svg>
        <span>+00 123 456 7890</span>
      </div>
      <div class="contact-line">
        <svg viewBox="0 0 16 16"><path d="M1 3h14v10H1zm1.5 1.5v.3L8 9l5.5-4.2v-.3z"/></svg>
        <span>hello@tidewatersys.com</span>
      </div>
      <div class="contact-line">
        <svg viewBox="0 0 16 16"><circle cx="8" cy="8" r="6.5"/><path d="M1.5 8h13M8 1.5v13M3 4.5h10M3 11.5h10" stroke="#fff" stroke-width="0.9" fill="none"/></svg>
        <span>www.tidewatersys.com</span>
      </div>
      <div class="address">Your Long Commercial or<br>business address in 2 line</div>
    </section>

    <svg class="footer-waves" viewBox="0 950 754 116" preserveAspectRatio="none">
      <path d="M0 960 Q 260 1005 525 1045 Q 290 1028 0 988 Z" fill="var(--brand-sky)"/>
      <path d="M0 993 Q 300 1042 754 1066 L 0 1066 Z" fill="var(--brand-ocean)"/>
    </svg>
  </main>
</body>
</html>
```